Business card design for Plumbing and Gas fitting company

We need a business card design for our plumbing and gas fitting company using the company logo and director details. Design should be modern and eye-catching however kept reasonably simple. This design should be targeted at commercial businesses/work so professionalism is key.

Target Market(s)

Commercial/business

Industry/Entity Type

Plumbing

Contact Information for Business Card

Warren Dohey
Director
027 581 9043
warren@vantorplumbingandgas.example
PO Box 7816
Palmerston North 4472

Font styles to use
Sans Serif

Requirements
Must have
• Logo
• Modern
• Kept simple
Nice to have
• Colour scheme based around logo

```html
<!DOCTYPE html>
<html lang="en">
<head>
<meta charset="utf-8">
<title>Vantor Plumbing &amp; Gas – Business Card</title>
<link rel="stylesheet" href="https://fonts.googleapis.com/css2?family=Lato:wght@400;700;900&display=swap">
<style>
  :root {
    --page-bg: #e9eaec;
    --card-bg: #ffffff;
    --brand-blue: #1a6fc1;
    --brand-orange: #ee7a2d;
    --ink: #1e1e1e;
    --card-shadow: rgba(0, 0, 0, 0.18);
  }
  * { margin: 0; padding: 0; box-sizing: border-box; }
  html, body {
    width: 1200px;
    height: 1000px;
    overflow: hidden;
    background: var(--page-bg);
    font-family: "Lato", Arial, sans-serif;
    color: var(--ink);
  }
  .canvas { position: relative; width: 1200px; height: 1000px; }

  .card {
    position: absolute;
    width: 640px;
    height: 370px;
    background: var(--card-bg);
    box-shadow: 0 10px 30px var(--card-shadow);
  }
  .card--front { left: 70px; top: 60px; display: flex; align-items: center; justify-content: center; }
  .card--back { left: 490px; top: 570px; }

  .brand-name {
    font-weight: 900;
    color: var(--brand-blue);
    letter-spacing: 0.2px;
    white-space: nowrap;
  }
  .card--front .brand-name { font-size: 40px; }
  .card--back .brand-name {
    position: absolute;
    top: 34px;
    right: 36px;
    font-size: 24px;
  }

  .contact {
    position: absolute;
    left: 0;
    top: 190px;
  }
  .contact-group {
    position: relative;
    padding-left: 40px;
    margin-bottom: 14px;
  }
  .contact-group::before {
    content: "";
    position: absolute;
    left: 0;
    top: 2px;
    bottom: 2px;
    width: 12px;
    background: var(--brand-blue);
  }
  .person-name { font-size: 26px; font-weight: 400; color: var(--brand-blue); line-height: 1.05; }
  .person-role { font-size: 14px; font-weight: 700; }
  .address { font-size: 15px; line-height: 1.3; }
  .contact-line { display: flex; align-items: center; gap: 10px; font-size: 15px; line-height: 1.6; }
  .contact-icon { width: 14px; height: 14px; flex: none; }
</style>
</head>
<body>
<main class="canvas">
  <section class="card card--front" aria-label="Card front">
    <span class="brand-name">Vantor Plumbing &amp; Gas</span>
  </section>

  <section class="card card--back" aria-label="Card back">
    <span class="brand-name">Vantor Plumbing &amp; Gas</span>

    <div class="contact">
      <div class="contact-group">
        <p class="person-name">Warren Dohey</p>
        <p class="person-role">Director</p>
      </div>
      <div class="contact-group">
        <p class="address">PO Box 7816<br>Palmerston North 4472</p>
      </div>
      <div class="contact-group">
        <p class="contact-line">
          <svg class="contact-icon" viewBox="0 0 16 16" aria-hidden="true"><path fill="var(--brand-orange)" d="M3.6 1.5l2.2 2.6-1.3 1.6c.9 2 2.6 3.7 4.6 4.6l1.6-1.3 2.6 2.2-1.4 2.3C6.6 14.9 1.1 9.4 1.3 2.9z"/></svg>
          027 581 9043
        </p>
        <p class="contact-line">
          <svg class="contact-icon" viewBox="0 0 16 16" aria-hidden="true"><rect x="1" y="3" width="14" height="10" fill="var(--brand-blue)"/><path d="M1 3.5l7 5 7-5" fill="none" stroke="#fff" stroke-width="1.3"/></svg>
          warren@vantorplumbingandgas.example
        </p>
        <p class="contact-line">
          <svg class="contact-icon" viewBox="0 0 16 16" aria-hidden="true"><circle cx="8" cy="8" r="7" fill="var(--brand-orange)"/><path d="M1 8h14M8 1c-3 3.5-3 10.5 0 14M8 1c3 3.5 3 10.5 0 14" fill="none" stroke="#fff" stroke-width="1"/></svg>
          www.vantorplumbingandgas.example
        </p>
      </div>
    </div>
  </section>
</main>
</body>
</html>
```